Innovative Water AWESOME Packaging Design

Hi everyone. Enjoy the brief!

WHO WE ARE:
We are a French beverage company focusing on innovative products in order to break into the market. Our mission? We are resolved to give a serious kick to the fusty Water market!  The product will be sold in many countries, including the USA.

WHY WE NEED YOU:
We are convinced that a great brand identity and packaging design are key elements to bring an innovative and novelty touch to our product. 
We definitely need your help!

WHAT WE DO:
Brisk & Bloomed Waters, known as B&B Waters, is a sparkling spring water infused with organic fruit & plants, enriched in vitamins and antioxydants. It comes in a 70cl trendy glass bottle.

Our first flavor is B&B Waters Lemon / Jasmin. 
Color is transparent like water slightly yellow tainted, but crystal clear. You can see through.

We have a real high end positionning, almost luxury, but modern and young. In addition the product will have the Organic certification (USDA). It will then be distributed in Organic grocery stores, selected high-end selling points, delicatessen and five star hotels.

To help you identify our space we could say that we consider our products in the TORVANE market space. (see inspirations attached)

YOUR MISSION:
1) Create a stunning and unique packaging design capable of creating awareness on its own.

2) To do so use the bottle attached and give life to our drinks.

3) Remember we are selling a unique, innovative and modern WATER. Not a drink, not a juice...The design will be better if you do not show fruits!!!

4) B&B Waters will be our logo. We would like the logo to be part of the label structure. The label has to be long and thin. See pictures called "inspiration" attached. 
We would like you to use the slender aspect of the letter "F" in the design architecture which we believe will give a touch of modernity and will be aligned with our positionning.

THE TEXT THAT WILL APPEAR ON THE PACKAGE:

Front label, from Up to Bottom:

B&B Waters
brisk and bloomed waters (optional)
sparkling
lemon & jasmin
enriched in C vitamin and antioxydants
50cl

Back label, from Up to Bottom:

B&B Waters (logo version)

(Text :)
La fraîcheur d’une infusion
de citron fraîchement pressée
délicieusement sublimée
par une note de jasmin.

Naturellement légère et
faible en calories cette
subtile association de saveurs
est enrichie en vitamines C
.

(Icons + text :)
Low calories
Spring water
Organic fruit infusion

No preservatives
No artificial sweeteners

USDA logo (see attached file)

Bar code space + Nutrition fact (see attached file)

WHAT WE WANT:

- A design that reflects our high end positionning
- A use of the letter F as part of the architecture
- A slender (thin and long) label and design
- An uncluttered, very simple and minimalistic design (see inspirations attached)
- To reflect an impression of modernity and novelty
- An instant feel of a luxury product

- The use of blue as our main color in order to stay in the WATER space (dark, light... whatever suits you)
- The use of colors to illustrate the flavors. NO FRUITS
- The use of a distinct font
- Highlight the logo and the word WATERS

WHAT WE DON'T WANT:
- We don't want a design that won't position us as an upmarket water brand
- We don't want our product to look like a drink made of juice or a soda
- We don't want to see the image of a fruit
- We don't want the design to be clutered or bold

This is all you need I guess! 
Thank you very much for your participation. We appreciate the time and energy you will put into designing our packaging. 

A big thank you from France.

Kind regards, 

Gaëtan and Ulric from B&B Bev.

Target Market(s)

Our clients are men and women mostly between 25 and 40 years old. Good purchasing power.

We would like the design to be modern and stylish.

Industry/Entity Type

Architecture

Font styles to use
Serif
Sans Serif

Colors
fdfeff
0255a3
3377b5
85acd3
86cae6
33a6d7
0492cd
cee9f5
cfdfed

Requirements
Must have
• WHAT WE WANT:

Nice to have
• Use the bars of B&B to structure your label and make it unique. See inspiration on TORVANE and Q milk (files called "inspiration).

They have a great use of the font and the logo it self determines the label structure.

This is our top priority.

Second is to reflect our upmarket positionning through a modern aspect.

Should not have
• WHAT WE DON'T WANT:

```html
<!DOCTYPE html>
<html lang="en">
<head>
<meta charset="utf-8">
<title>B&amp;B Waters — Front Label Options</title>
<link rel="stylesheet" href="https://fonts.googleapis.com/css2?family=Raleway:wght@300;400;600;700&family=Arimo:wght@400&display=swap">
<style>
  :root {
    --stage: #e4e4e5;
    --water-tint: #f4f5cf;
    --water-edge: #e9ebb4;
    --navy: #0255a3;
    --mid-blue: #3377b5;
    --sky: #33a6d7;
    --cyan: #0492cd;
    --mist: #cfdfed;
    --ink: #3d3d3f;
    --soft-ink: #6d6d6a;
    --white: #fdfeff;
  }
  * { margin: 0; padding: 0; box-sizing: border-box; }
  html, body { width: 886px; height: 1200px; overflow: hidden; }
  body {
    position: relative;
    background: var(--stage);
    font-family: "Raleway", sans-serif;
    color: var(--ink);
  }
  .label-shapes { position: absolute; inset: 0; }
  .abs { position: absolute; }

  .logo-caption {
    left: 570px; top: 42px;
    font-family: "Arimo", sans-serif; font-size: 17px; color: #111;
  }
  .logo-lockup {
    left: 700px; top: 60px; width: 150px;
    display: flex; flex-direction: column; align-items: center; gap: 8px;
  }
  .logo-lockup .mark {
    width: 82px; height: 82px; border-radius: 50%;
    border: 2px solid var(--ink);
  }
  .logo-lockup .name {
    font-weight: 700; font-size: 26px; letter-spacing: 0.5px; color: var(--ink);
  }

  .brand-vertical {
    left: 290px; top: 490px;
    transform: translate(-50%, -50%) rotate(-90deg);
    white-space: nowrap;
    font-weight: 700; font-size: 14px; letter-spacing: 1.5px; color: var(--white);
  }
  .flavour-vertical {
    left: 290px; top: 668px;
    transform: translate(-50%, -50%) rotate(-90deg);
    white-space: nowrap;
    font-size: 12.5px; letter-spacing: 0.6px; color: var(--white);
  }
  .flavour-vertical b { font-weight: 700; }
  .flavour-vertical span { font-weight: 300; }

  .brand-drop {
    left: 500px; top: 412px; width: 100px;
    display: flex; align-items: center; justify-content: center; gap: 6px;
    font-weight: 700; font-size: 18px; color: var(--ink);
  }
  .brand-drop .dot {
    width: 14px; height: 14px; border-radius: 50%; border: 1.5px solid var(--ink);
  }
  .flavour-stack {
    left: 490px; top: 512px; width: 122px;
    text-align: center; font-size: 11px; line-height: 13px; color: var(--white);
  }
  .flavour-stack b { font-weight: 700; letter-spacing: 0.3px; }
  .flavour-stack span { font-weight: 300; letter-spacing: 0.5px; }

  .claim {
    width: 160px; text-align: center;
    font-weight: 400; font-size: 10.5px; line-height: 13px; color: var(--soft-ink);
  }
  .claim.one { left: 216px; top: 838px; }
  .claim.two { left: 470px; top: 838px; }
  .volume {
    width: 60px; text-align: center; font-size: 10px; color: var(--soft-ink);
  }
  .volume.one { left: 266px; top: 917px; }
  .volume.two { left: 520px; top: 917px; }

  .view-caption {
    top: 1094px; font-family: "Arimo", sans-serif; font-size: 20px; color: #111;
  }
  .view-caption.one { left: 203px; }
  .view-caption.two { left: 490px; }
</style>
</head>
<body>
  <svg class="label-shapes" width="886" height="1200" viewBox="0 0 886 1200">
    <defs>
      <linearGradient id="fade-blue" x1="0" y1="0" x2="0" y2="1">
        <stop offset="0" stop-color="#0492cd"/>
        <stop offset="0.45" stop-color="#5fb8dc"/>
        <stop offset="1" stop-color="#dfeee0"/>
      </linearGradient>
    </defs>
    <!-- label grounds, option 1 and option 2 -->
    <rect x="192" y="250" width="208" height="800" rx="26" fill="var(--water-tint)" stroke="var(--water-edge)"/>
    <rect x="446" y="250" width="208" height="800" rx="26" fill="var(--water-tint)" stroke="var(--water-edge)"/>
    <!-- option 1: slender spike -->
    <polygon points="290,335 322,600 258,600" fill="var(--navy)"/>
    <polygon points="258,600 322,600 322,762 290,792 258,762" fill="var(--sky)"/>
    <!-- option 2: tapering band -->
    <polygon points="490,505 612,505 551,792" fill="url(#fade-blue)"/>
  </svg>

  <div class="abs logo-caption">Logo option 2</div>
  <div class="abs logo-lockup">
    <div class="mark"></div>
    <div class="name">B&amp;B WATERS</div>
  </div>

  <div class="abs brand-vertical">B&amp;B WATERS</div>
  <div class="abs flavour-vertical"><b>SPARKLING</b> <span>LEMON &amp; JASMIN</span></div>

  <div class="abs brand-drop"><span class="dot"></span>B&amp;B</div>
  <div class="abs flavour-stack"><b>SPARKLING</b><br><span>LEMON &amp;<br>JASMIN</span></div>

  <p class="abs claim one">Enriched In C Vitamin<br>And Antioxidants</p>
  <p class="abs claim two">Enriched In C Vitamin<br>And Antioxidants</p>
  <p class="abs volume one">50cl</p>
  <p class="abs volume two">50cl</p>

  <p class="abs view-caption one">Front view&nbsp; option 1</p>
  <p class="abs view-caption two">Front view&nbsp; option 2</p>
</body>
</html>
```